creative pack design with extended budget for Nobrelia coffee product

- we need a packing design for a new product of coffee for our company Mbelo Tiru located in Uganda.
- specialty Arabica coffee grown at slopes of Mountain Elgon with rich volcanic soils located in Eastern region of Uganda.
-  we have a logo already made and has registered in Uganda. our logo colors are mixture between a lot of brown color and yellow. vacuum  plastic bags.
- there is no restrictions towards your imagination .
-  all details available
- we will launch our product through phases ;
- phase 1 is  a ground coffee : ( Turkish coffee )  2 degrees of roasting which are ( medium dark , light ) of 250 grm
b) roasted beans: 2 degrees ( medium, dark) of 250 grm & 1000 grm
- we need also to highlight the eastern spirit of Turkish coffee
- we  need designs, the info and color only will be changed depending on previous classifications

Target Market(s)
Arab countries, Turkey , Uganda, Europe
Colors
Designer to choose colors to be used in the design.
Requirements
Nice to have
- about nature , Elgon mountain , farmers, freshness, distinctive product, soul of east such as decorated cup of Turkish coffee . these just an ideas but there is no restrictions on your imagination

```html
<!DOCTYPE html>
<html lang="en">
<head>
<meta charset="utf-8">
<title>Nobrelia Arabica – Pack Design</title>
<link href="https://fonts.googleapis.com/css2?family=Lilita+One&family=Poppins:wght@500;600&family=PT+Sans+Narrow:wght@400;700&display=swap" rel="stylesheet">
<style>
  :root{
    --paper:#ece1c8;
    --brown-dark:#4a2816;
    --brown-text:#5b3318;
    --brown-mid:#6e4526;
    --tan:#a98657;
    --tan-light:#c9ab7c;
    --leaf-mix:#8a6a45;
    --cream:#f6eedd;
    --white:#ffffff;
    --rule:#c8b89a;
  }
  *{box-sizing:border-box;margin:0;padding:0}
  html,body{width:1080px;height:1200px;overflow:hidden;background:var(--white)}
  .pack{
    position:absolute;left:47px;top:37px;width:986px;height:1126px;
    display:flex;border:1px solid var(--rule);background:var(--paper);
  }
  .panel{position:relative;height:100%;border-right:1px solid var(--rule);overflow:hidden}
  .panel:last-child{border-right:none}
  .panel--side{width:270px}
  .panel--front{width:446px}

  /* lower bands */
  .band-rule{position:absolute;left:0;right:0;height:16px;background:var(--tan)}
  .band-rule--top{top:703px}
  .band-rule--bottom{top:797px}
  .band-leaves{
    position:absolute;left:0;right:0;top:719px;height:78px;
    background:linear-gradient(90deg,var(--brown-mid) 0%,var(--leaf-mix) 25%,#6a4a2c 50%,var(--leaf-mix) 75%,var(--brown-mid) 100%);
  }
  .band-beans{
    position:absolute;left:0;right:0;top:813px;bottom:0;
    background:
      radial-gradient(ellipse at 30% 30%,rgba(140,90,50,.55) 0%,rgba(140,90,50,0) 45%),
      radial-gradient(ellipse at 75% 75%,rgba(140,90,50,.5) 0%,rgba(140,90,50,0) 45%),
      linear-gradient(180deg,#5c361d 0%,var(--brown-dark) 100%);
  }

  /* brand name stand-in */
  .brand{position:absolute;left:50%;transform:translateX(-50%);display:flex;flex-direction:column;align-items:center}
  .brand__dot{border-radius:50%;background:var(--brown-dark)}
  .brand__name{font-family:"Poppins",sans-serif;font-weight:600;color:var(--brown-text);letter-spacing:.04em}
  .brand--small{top:120px}
  .brand--small .brand__dot{width:46px;height:46px}
  .brand--small .brand__name{font-size:17px;margin-top:6px}
  .brand--large{top:620px;width:264px;height:264px;border-radius:50%;background:var(--brown-dark);border:8px solid var(--cream);box-shadow:0 0 0 5px var(--brown-dark);justify-content:center}
  .brand--large .brand__name{font-size:40px;color:var(--cream);letter-spacing:.02em}

  /* type */
  .title{position:absolute;left:0;right:0;text-align:center;font-family:"Lilita One",sans-serif;color:var(--brown-text);letter-spacing:.06em;line-height:1}
  .title--side{top:228px;font-size:46px}
  .title--front{top:442px;font-size:80px}
  .subtitle{position:absolute;left:0;right:0;text-align:center;font-family:"Poppins",sans-serif;font-weight:500;color:var(--brown-text);line-height:1}
  .subtitle--side{top:279px;font-size:15px}
  .subtitle--front{top:532px;font-size:27px}
  .origin{position:absolute;left:0;right:0;text-align:center;font-family:"Poppins",sans-serif;font-weight:600;line-height:1}
  .origin--side{top:304px;font-size:15px;color:var(--brown-text)}
  .origin--front{top:918px;font-size:27px;color:var(--white);letter-spacing:.04em}

  .copy{position:absolute;left:32px;right:32px;text-align:center;font-family:"PT Sans Narrow",sans-serif;font-size:16.5px;line-height:22.6px;color:var(--brown-text)}
  .copy__name{font-weight:700;font-size:20px;line-height:26px;color:var(--brown-dark)}
  .copy__lead{font-weight:700;color:var(--brown-dark)}
  .copy--left{top:336px}
  .copy--left .copy__body{margin-top:14px}
  .copy--right{top:340px}

  .weight{position:absolute;left:0;right:0;top:1008px;text-align:center;font-family:"Poppins",sans-serif;font-weight:600;font-size:34px;color:var(--white);line-height:1}
  .weight small{font-size:25px;margin-left:6px}

  /* front illustration areas */
  .scene{position:absolute;left:121px;top:0;width:209px;height:325px;border-radius:0 0 104px 104px;background:linear-gradient(180deg,var(--brown-dark) 0%,#6b4526 45%,var(--tan) 80%,var(--tan-light) 100%);border:4px solid var(--brown-dark);border-top:none}
  .cup{position:absolute;left:112px;top:258px;width:228px;height:150px;border-radius:28px;background:linear-gradient(180deg,var(--cream) 0%,var(--tan-light) 60%,var(--tan) 100%);box-shadow:0 0 0 3px var(--brown-text)}

  /* roast scale */
  .roast{position:absolute;left:34px;top:653px;display:flex;align-items:center;gap:12px}
  .roast__label{font-family:"Poppins",sans-serif;font-weight:500;font-size:15px;line-height:16px;color:var(--brown-dark);text-align:center}
</style>
</head>
<body>
<main class="pack">

  <section class="panel panel--side panel--left">
    <div class="brand brand--small"><span class="brand__dot"></span><span class="brand__name">Nobrelia</span></div>
    <h2 class="title title--side">ARABICA</h2>
    <p class="subtitle subtitle--side">roasted coffee beans</p>
    <p class="origin origin--side">UGANDA</p>
    <div class="copy copy--left">
      <p class="copy__name">Mbelo Tiru</p>
      <p class="copy__lead">Specialty Arabica coffee grown at slopes of Mountain Elgon with rich volcanic soils located in Eastern region of Uganda.</p>
      <p class="copy__body">Specialty Arabica coffee grown at slopes of Mountain Elgon with rich volcanic soils located in Eastern region of Uganda. Specialty Arabica coffee grown slopes of Mountain Elgon with rich volcanic soils located in Eastern region</p>
    </div>
    <div class="band-rule band-rule--top"></div>
    <div class="band-leaves" role="img" aria-label="Pattern of coffee leaves"></div>
    <div class="band-rule band-rule--bottom"></div>
    <div class="band-beans" role="img" aria-label="Pattern of scattered coffee beans"></div>
    <p class="weight">250<small>g</small></p>
  </section>

  <section class="panel panel--front">
    <div class="scene" role="img" aria-label="Illustration of the sun over Mount Elgon and acacia trees"></div>
    <div class="cup" role="img" aria-label="Illustration of a coffee cup surrounded by roasted beans"></div>
    <h1 class="title title--front">ARABICA</h1>
    <p class="subtitle subtitle--front">roasted coffee beans</p>
    <div class="band-rule band-rule--top"></div>
    <div class="band-leaves" role="img" aria-label="Pattern of coffee leaves"></div>
    <div class="band-rule band-rule--bottom"></div>
    <div class="band-beans" role="img" aria-label="Pattern of scattered coffee beans"></div>
    <div class="brand brand--large"><span class="brand__name">Nobrelia</span></div>
    <p class="origin origin--front">UGANDA</p>
    <p class="weight">250<small>g</small></p>
  </section>

  <section class="panel panel--side panel--right">
    <div class="brand brand--small"><span class="brand__dot"></span><span class="brand__name">Nobrelia</span></div>
    <h2 class="title title--side">ARABICA</h2>
    <p class="subtitle subtitle--side">roasted coffee beans</p>
    <p class="origin origin--side">UGANDA</p>
    <p class="copy copy--right">Specialty Arabica coffee grown at slopes of Mountain Elgon with rich volcanic soils located in Eastern region of Uganda. Specialty Arabica coffee grown slopes of Mountain Elgon with rich volcanic soils located in Eastern region specialty Arabica coffee grown at slopes of Mountain Elgon with rich volcanic soils located in Eastern region of Uganda.</p>
    <div class="roast">
      <p class="roast__label">Roasting<br>degrees</p>
      <svg class="roast__scale" width="94" height="26" viewBox="0 0 94 26" role="img" aria-label="Roast level 3 of 5">
        <g stroke="#4a2816" stroke-width="1.4">
          <ellipse cx="9" cy="13" rx="7" ry="11" fill="#4a2816"/>
          <ellipse cx="28" cy="13" rx="7" ry="11" fill="#4a2816"/>
          <ellipse cx="47" cy="13" rx="7" ry="11" fill="#4a2816"/>
          <ellipse cx="66" cy="13" rx="7" ry="11" fill="none"/>
          <ellipse cx="85" cy="13" rx="7" ry="11" fill="none"/>
        </g>
        <g stroke="#ece1c8" stroke-width="1.2" fill="none">
          <path d="M9 3 Q6 13 9 23"/><path d="M28 3 Q25 13 28 23"/><path d="M47 3 Q44 13 47 23"/>
        </g>
        <g stroke="#4a2816" stroke-width="1.2" fill="none">
          <path d="M66 3 Q63 13 66 23"/><path d="M85 3 Q82 13 85 23"/>
        </g>
      </svg>
    </div>
    <div class="band-rule band-rule--top"></div>
    <div class="band-leaves" role="img" aria-label="Pattern of coffee leaves"></div>
    <div class="band-rule band-rule--bottom"></div>
    <div class="band-beans" role="img" aria-label="Pattern of scattered coffee beans"></div>
    <p class="weight">250<small>g</small></p>
  </section>

</main>
</body>
</html>
```